" ESCRITORIO DE SERVICO CONSULTIVO PROVIDO POR PROFISSIONAIS COM AMPLA EXPERIENCIA NO SETOR ELETRICO COM ATUACAO ACIMA DE 13 ANOS DE EXPERIENCIA. ATUMOS ATRAVES DO ENGAJAMENTO DE AGENTES A PARTIR DE CONSULTA DA NECESSIDADE E ELABORACAO DE PACOTE DE SERVICOS ALINHADO A EXPECTATIVA DO CLIENTE. SERVICOS PRINCIPAIS: GESTAO DE PLEITOS DE CONTRATOS DE GERACAO, TRANSMISSAO E DISTRIBUICAO DE ENERGIA GESTAO DE PROCESSOS DE AQUISICAO DE EQUIPAMENTOS E SERVICOS PARA EMPREENDIMENTOS DE GERACAO, TRANSMISSAO E DISTRIBUICAO DE ENERGIA OUTROS SERVICOS: PLANEJAMENTO E GESTAO DE EMPREENDIMENTOS DE GERACAO, TRANSMISSAO E DISTRIBUICAO DE ENERGIA "

```html
<!DOCTYPE html>
<html lang="pt-BR">
<head>
<meta charset="UTF-8">
<title>Norvale Consulting – Cartão de Visita</title>
<link href="https://fonts.googleapis.com/css2?family=Montserrat:wght@400;500;700;800&display=swap" rel="stylesheet">
<style>
  :root{
    --bg:#e9eaec;
    --card:#ffffff;
    --ink:#2f343d;
    --dark-band:#363b45;
    --accent:#e9a317;
    --soft-grey:#d5d7da;
    --muted:#8b8f96;
    --light-text:#f3f4f6;
  }
  *{box-sizing:border-box;margin:0;padding:0}
  html,body{width:1200px;height:1200px;overflow:hidden}
  body{
    background:var(--bg);
    font-family:"Montserrat",Arial,sans-serif;
    color:var(--ink);
    display:flex;flex-direction:column;align-items:center;justify-content:center;gap:64px;
  }
  .card{
    width:880px;height:503px;background:var(--card);
    position:relative;overflow:hidden;
    box-shadow:0 14px 36px rgba(0,0,0,.18);
  }

  /* ---------- Front ---------- */
  .front .brand{
    position:absolute;left:70px;top:88px;
    display:flex;align-items:center;gap:16px;
  }
  .brand-dot{width:30px;height:30px;background:var(--accent)}
  .brand-name{
    font-weight:800;color:var(--ink);line-height:1.05;text-transform:uppercase;
  }
  .front .brand-name{font-size:34px;letter-spacing:3px}
  .front .brand-name small{display:block;font-size:13px;letter-spacing:9px;font-weight:800}

  .holder{position:absolute;right:120px;top:96px;text-align:center}
  .holder-name{font-weight:800;font-size:26px;letter-spacing:.5px}
  .holder-role{font-size:12px;color:var(--muted);letter-spacing:2px;margin-top:14px;font-weight:500}

  .accent-line{position:absolute;left:0;right:0;top:236px;height:4px;background:var(--soft-grey)}
  .dark-band{
    position:absolute;left:0;right:0;top:246px;bottom:0;background:var(--dark-band);
  }
  .contacts{
    position:absolute;left:70px;right:60px;top:290px;
    display:grid;grid-template-columns:1fr 1.15fr;column-gap:40px;
    color:var(--light-text);
  }
  .contact-list{list-style:none;display:flex;flex-direction:column;gap:18px}
  .contact-item{display:flex;align-items:flex-start;gap:16px;font-size:20px;font-weight:500;line-height:1.2}
  .contact-item svg{flex:none;width:22px;height:22px;margin-top:2px}
  .contact-item .address{font-size:15px;font-weight:400;line-height:1.35}
  .social-mark{flex:none;width:20px;height:20px;border-radius:50%;background:var(--accent);margin-top:2px}

  /* ---------- Back ---------- */
  .back .grey-band{
    position:absolute;left:0;right:0;top:150px;height:240px;
    background:linear-gradient(90deg,#ffffff 0%,#e3e4e6 45%,#cfd1d4 100%);
  }
  .back .brand{
    position:absolute;inset:0;display:flex;align-items:center;justify-content:center;gap:26px;
  }
  .back .brand-dot{width:56px;height:56px}
  .back .brand-name{font-size:72px;letter-spacing:6px;text-align:center}
  .back .brand-name small{display:block;font-size:22px;letter-spacing:17px;margin-top:6px}
</style>
</head>
<body>

  <section class="card front" aria-label="Frente do cartão">
    <div class="brand">
      <span class="brand-dot"></span>
      <div class="brand-name">Norvale<small>Consulting</small></div>
    </div>

    <div class="holder">
      <p class="holder-name">NOME SOBRENOME</p>
      <p class="holder-role">FUNÇÃO</p>
    </div>

    <div class="accent-line"></div>
    <div class="dark-band"></div>

    <div class="contacts">
      <ul class="contact-list">
        <li class="contact-item">
          <svg viewBox="0 0 24 24" fill="none" stroke="#f3f4f6" stroke-width="2"><rect x="3" y="5" width="18" height="14" rx="1"/><path d="M3 6l9 7 9-7"/></svg>
          <span>empresa@.com.br</span>
        </li>
        <li class="contact-item">
          <svg viewBox="0 0 24 24" fill="#f3f4f6"><path d="M6.6 10.8a15 15 0 0 0 6.6 6.6l2.2-2.2a1 1 0 0 1 1-.25 11.4 11.4 0 0 0 3.6.57 1 1 0 0 1 1 1V20a1 1 0 0 1-1 1A17 17 0 0 1 3 4a1 1 0 0 1 1-1h3.5a1 1 0 0 1 1 1c0 1.25.2 2.45.57 3.6a1 1 0 0 1-.25 1z"/></svg>
          <span>(11) 0000-0000<br>(11) 00000-0000</span>
        </li>
        <li class="contact-item">
          <span class="social-mark"></span>
          <span>@empresa</span>
        </li>
      </ul>

      <ul class="contact-list">
        <li class="contact-item">
          <svg viewBox="0 0 24 24" fill="none" stroke="#f3f4f6" stroke-width="2"><circle cx="12" cy="12" r="9"/><path d="M3 12h18M12 3c3 3.5 3 14.5 0 18M12 3c-3 3.5-3 14.5 0 18"/></svg>
          <span>www.empresa.com.br</span>
        </li>
        <li class="contact-item">
          <svg viewBox="0 0 24 24" fill="#f3f4f6"><path d="M12 2a7 7 0 0 0-7 7c0 5.2 7 13 7 13s7-7.8 7-13a7 7 0 0 0-7-7zm0 9.5A2.5 2.5 0 1 1 12 6.5a2.5 2.5 0 0 1 0 5z"/></svg>
          <span class="address">Rua do projeto, 00 Centro -<br>Cidade - Estado - Cep 00.000-000</span>
        </li>
        <li class="contact-item">
          <span class="social-mark"></span>
          <span>empresa</span>
        </li>
      </ul>
    </div>
  </section>

  <section class="card back" aria-label="Verso do cartão">
    <div class="grey-band"></div>
    <div class="brand">
      <span class="brand-dot"></span>
      <div class="brand-name">Norvale<small>Consulting</small></div>
    </div>
  </section>

</body>
</html>
```